Interfaith Forum and Festival Postcard style Flyer

Create a Post Card Design: 6x9

Unity Teen Assembly of Harbor Valley's Annual Spirit Summit and Fair: Teens expressing their Faith Through Art, Music, & Dialogue.
Westmere Institute 27415 Larkfield Suite 100 Irvine, CA 92614
11:30am-9:00pm
UTAHV.org
like us on Sampleface https://www.sampleface.net/UTAHV/
Contact Person: Rohanpreet Sandhu UTAHVorg@mailbox.example

Task:
We are hosting our 12th annual Crossroads Teen Summit in Orange County. It is also the 3rd annual Spirit Fair.
We are looking for a large postcard like flyer front and back that will highlight our event that we can send out
Please include our UTAHV logo as well as our Bright Harbor Allies logo
Please feel free to clean up/crop pics if necessary

Additional Info to include:
• RSVP for our SPIRIT SUMMIT by February 1st, 2016
• To Participate in our Spirit Fair (Music, Song, Dance) RSVP by February 12th, 2016
• Art work Must be Submitted by: March 1st, 2015

(High School Students only)

Useful Background info (not necessary to include):

http://utahv.org/about/

Crossroads Teen Summit
This year's theme "Shared Horizons"
All high school age faith groups are invited to come and join with 100 to 150 other high school students from various faith traditions to participate in the Unity Teen Assembly of Harbor Valley‘s Annual Crossroads Teen Summit.
The purpose of this Crossroads Teen Summit is to bring together young people from diverse ethnic, cultural, and religious backgrounds, and to engage them in dialogue. True dialogue is a conversation on a common subject between two or more persons of differing points of view and/or backgrounds. This dialogue’s purpose is two-fold: first, for each participant to learn from the other so that he or she can understand and grow; second, for each participating adult to learn from the young what they think, what their concerns are, and how they deal with differing points of view. We feel that this commitment to dialogue will affect relationships in a constructive way in our places of worship and in our community.
The forum itself involves having eight high school-age kids and one adult youth leader around each table to discuss a common question.
Our intent is to make each discussion group as religiously diverse as possible. Our youth leaders act as facilitators, but it is stressed that it is the students we want to hear from. The facilitator is there only to encourage the dialogue.
The forum will be followed by the Spirit Fair where families of the participants are welcomed to join. This event will include and Art gallery display of the teens, highlighting their expressions of faith

Target Market(s)

Youth and Interfaith Organizations and Places of Worship

Industry/Entity Type

Festival

Colors
f37022
faa54b
f78f20

Requirements
Must have
• Both Logos
• Unity Teen Assembly of Harbor Valley's Annual Spirit Summit and Fair: Teens expressing their Faith Through Art, Music, & Dialogue.
• Westmere Institute 27415 Larkfield Suite 100 Irvine, CA 92614
• 11:30am-9:00pm
• UTAHV.org
• like us on Sampleface https://www.sampleface.net/UTAHV/
• Contact Person: Rohanpreet Sandhu UTAHVorg@mailbox.example
• RSVP Info (please look at Project description)
Should not have
• does not need to include all the background info

```html
<!DOCTYPE html>
<html lang="en">
<head>
<meta charset="utf-8">
<title>Unity Teen Assembly of Harbor Valley – Spirit Summit and Fair Postcard</title>
<link rel="stylesheet" href="https://fonts.googleapis.com/css2?family=Oswald:wght@400;500;600;700&family=Lato:wght@400;700;900&display=swap">
<style>
  :root{
    --orange:#f37022;
    --orange-mid:#f78f20;
    --orange-light:#faa54b;
    --dark:#262324;
    --dark-2:#343132;
    --ink:#333;
    --white:#fff;
    --paper:#e6e6e6;
    --photo-green:#6f7f4e;
    --photo-warm:#8a5a3c;
    --photo-sky:#c8a98a;
  }
  *{box-sizing:border-box;margin:0;padding:0}
  html,body{width:806px;height:1200px;overflow:hidden}
  body{background:var(--paper);font-family:"Lato",sans-serif;position:relative}
  .card{position:absolute;left:57px;width:693px;background:var(--white);overflow:hidden;box-shadow:0 4px 10px rgba(0,0,0,.35)}
  .front{top:91px;height:470px}
  .back{top:627px;height:466px}

  /* front */
  .front .side{position:absolute;left:0;top:0;width:204px;height:314px;background:linear-gradient(90deg,var(--dark) 0%,var(--dark-2) 100%)}
  .front .side-rule{position:absolute;left:196px;top:0;width:8px;height:314px;background:var(--orange)}
  .logo{position:absolute;left:54px;top:3px;width:96px;height:96px;border:2px solid var(--white);border-radius:50%;display:flex;align-items:center;justify-content:center;text-align:center;color:var(--white);font:700 10px/1.2 "Lato",sans-serif;padding:12px}
  .inset-photo{position:absolute;left:34px;top:162px;width:120px;height:120px;border-radius:50%;border:5px solid var(--orange);background:radial-gradient(circle at 50% 55%,#d9d3cf 0%,#9b8c86 60%,#5a4d49 100%)}
  .hero-photo{position:absolute;left:211px;top:0;width:482px;height:182px;background:linear-gradient(180deg,#7d8f5a 0%,var(--photo-green) 35%,#4d4a44 100%);border-bottom-left-radius:60px;border-left:7px solid var(--orange);border-bottom:7px solid var(--orange)}
  .title-block{position:absolute;left:204px;top:182px;width:489px;height:132px;background:linear-gradient(180deg,#2b2829,var(--dark))}
  .title-block h1{position:absolute;left:22px;top:24px;font:600 22px/1 "Oswald",sans-serif;color:var(--orange);letter-spacing:.2px;white-space:nowrap}
  .title-block .subtitle{position:absolute;left:22px;top:58px;font:400 17px/1 "Oswald",sans-serif;color:var(--white);letter-spacing:.6px;white-space:nowrap}
  .title-block .venue{position:absolute;left:22px;top:88px;width:450px;font:400 10.5px/1.4 "Lato",sans-serif;color:var(--white)}
  .title-block .venue b{color:var(--orange-light);font-weight:700}
  .promo{position:absolute;left:0;top:314px;width:521px;height:118px;background:linear-gradient(90deg,var(--orange) 0%,var(--orange-mid) 70%,var(--orange-light) 100%);border-top-right-radius:40px}
  .promo-edge{position:absolute;left:0;top:306px;width:535px;height:164px;background:var(--dark);border-top-right-radius:46px}
  .promo .tagline{position:absolute;left:14px;top:18px;font:600 13px/1 "Oswald",sans-serif;color:var(--white);letter-spacing:.4px}
  .promo .pill{position:absolute;left:0;top:45px;width:478px;height:27px;background:var(--dark);border-radius:0 14px 14px 0;padding-left:14px;display:flex;align-items:center;font:500 14px/1 "Oswald",sans-serif;color:var(--white);letter-spacing:.3px;white-space:nowrap}
  .promo .pill b{color:var(--orange-light);font-weight:600;margin-right:5px}
  .promo .also{position:absolute;left:14px;top:84px;font:400 18px/1 "Oswald",sans-serif;color:var(--white);letter-spacing:.4px;white-space:nowrap}
  .promo .also b{color:var(--dark);font-weight:700}
  .contact{position:absolute;display:flex;align-items:center;justify-content:space-between;color:var(--white);font:400 10.5px/1 "Lato",sans-serif;white-space:nowrap}
  .contact span{display:flex;align-items:center;gap:5px}
  .contact svg{width:10px;height:10px;fill:var(--orange)}
  .front .contact{left:14px;top:445px;width:500px}
  .partner{position:absolute;left:535px;top:314px;width:158px;height:156px;background:var(--white);text-align:center}
  .partner-mark{position:absolute;left:14px;top:20px;width:130px;display:flex;align-items:center;justify-content:center;gap:6px;font:400 15px/1.05 "Lato",sans-serif;color:#2f5b8f}
  .partner-mark i{width:22px;height:22px;border-radius:50%;border:1.5px solid #2f5b8f;flex:none}
  .social{position:absolute;left:0;right:0;top:90px;font:700 11px/1.35 "Lato",sans-serif;color:var(--dark)}
  .social em{font-style:normal;color:var(--orange)}

  /* back */
  .back .header{position:absolute;left:0;top:0;width:693px;height:225px;background:linear-gradient(90deg,var(--dark),var(--dark-2))}
  .back .header-rule{position:absolute;left:0;top:216px;width:693px;height:10px;background:linear-gradient(90deg,var(--orange),var(--orange-light))}
  .theme-label{position:absolute;left:14px;top:18px;font:600 27px/1 "Oswald",sans-serif;color:var(--orange);letter-spacing:.3px}
  .theme-name{position:absolute;left:14px;top:56px;font:400 23px/1 "Oswald",sans-serif;color:var(--white);letter-spacing:1px}
  .rsvp-pill{position:absolute;left:0;top:95px;width:258px;height:57px;background:linear-gradient(90deg,var(--orange),var(--orange-mid));border-radius:0 28px 28px 0;padding:8px 0 0 14px;color:var(--white)}
  .rsvp-pill .line1{font:500 16px/1.1 "Oswald",sans-serif;letter-spacing:.2px}
  .rsvp-pill .line2{font:400 16px/1.2 "Oswald",sans-serif}
  .rsvp-pill .line2 b{font-family:"Lato",sans-serif;font-weight:900}
  .fair-rsvp{position:absolute;left:14px;top:164px;font:700 11px/1.4 "Lato",sans-serif;color:var(--white)}
  .fair-rsvp b{color:var(--orange)}
  .team-photo{position:absolute;left:316px;top:0;width:377px;height:208px;background:linear-gradient(180deg,#6b4a3c 0%,var(--photo-warm) 45%,#5b5048 100%);border-left:7px solid var(--orange);border-bottom-left-radius:40px}
  .about{position:absolute;left:250px;top:246px;width:432px;font:400 11.3px/1.33 "Lato",sans-serif;color:var(--ink)}
  .about p{margin-bottom:6px}
  .art-photo{position:absolute;left:0;top:279px;width:238px;height:86px;background:linear-gradient(180deg,#8a7a70 0%,var(--photo-sky) 55%,#6b5a4e 100%)}
  .art-frame{position:absolute;left:0;top:270px;width:246px;height:170px;border-top:8px solid var(--dark);border-right:8px solid var(--dark);border-top-right-radius:36px}
  .art-box{position:absolute;left:0;top:365px;width:238px;height:69px;background:linear-gradient(90deg,var(--orange),var(--orange-mid));padding:6px 0 0 12px;color:var(--white);font-family:"Oswald",sans-serif;font-variant:small-caps;font-weight:700}
  .art-box .big{font-size:27px;line-height:.95;letter-spacing:.5px}
  .art-box .small{font-size:16px;line-height:1.05;letter-spacing:.3px}
  .back-bar{position:absolute;left:254px;top:436px;width:439px;height:30px;background:var(--dark)}
  .back .contact{left:272px;top:446px;width:400px}
</style>
</head>
<body>
<svg width="0" height="0" style="position:absolute">
  <symbol id="icon-phone" viewBox="0 0 24 24"><path d="M6.6 10.8a15.1 15.1 0 0 0 6.6 6.6l2.2-2.2c.3-.3.7-.4 1-.2 1.1.4 2.3.6 3.6.6.6 0 1 .4 1 1V20c0 .6-.4 1-1 1A17 17 0 0 1 3 4c0-.6.4-1 1-1h3.5c.6 0 1 .4 1 1 0 1.3.2 2.5.6 3.6.1.3 0 .7-.2 1z"/></symbol>
  <symbol id="icon-mail" viewBox="0 0 24 24"><path d="M2 5h20v14H2z M3 6l9 7 9-7" fill-rule="evenodd"/></symbol>
  <symbol id="icon-globe" viewBox="0 0 24 24"><circle cx="12" cy="12" r="10"/></symbol>
</svg>

<section class="card front">
  <div class="side"></div>
  <div class="side-rule"></div>
  <div class="logo">Unity Teen Assembly of Harbor Valley</div>
  <div class="inset-photo" role="img" aria-label="Photo of teens in discussion around a table"></div>
  <div class="hero-photo" role="img" aria-label="Group photo of teen participants on a lawn"></div>
  <div class="title-block">
    <h1>UNITY TEEN ASSEMBLY OF HARBOR VALLEY'S</h1>
    <p class="subtitle">ANNUAL SPIRIT SUMMIT AND FAIR</p>
    <p class="venue">Westmere Institute, 27415 Larkfield Suite 100 Irvine, CA 92614<br><b>11:30am – 9:00pm</b></p>
  </div>
  <div class="promo-edge"></div>
  <div class="promo">
    <div class="tagline">TEENS EXPRESSING THEIR FAITH THROUGH ART, MUSIC, &amp; DIALOGUE</div>
    <div class="pill"><b>12TH ANNUAL</b> CROSSROADS TEEN SUMMIT IN ORANGE COUNTY</div>
    <div class="also">IT IS ALSO THE <b>3RD</b> ANNUAL SPIRIT FAIR</div>
  </div>
  <div class="contact">
    <span>Rohanpreet Sandhu</span>
    <span><svg><use href="#icon-phone"/></svg>(555) 014-2288</span>
    <span><svg><use href="#icon-mail"/></svg>UTAHVorg@mailbox.example</span>
    <span><svg><use href="#icon-globe"/></svg>www.utahv.org</span>
  </div>
  <div class="partner">
    <div class="partner-mark">Bright Harbor Allies<i></i></div>
    <div class="social"><em>Like us on</em> Sampleface<br>www.sampleface.net/UTAHV/</div>
  </div>
</section>

<section class="card back">
  <div class="header"></div>
  <div class="header-rule"></div>
  <div class="theme-label">THIS YEAR'S THEME</div>
  <div class="theme-name">"SHARED HORIZONS"</div>
  <div class="rsvp-pill">
    <div class="line1">RSVP for our SPIRIT SUMMIT</div>
    <div class="line2">by <b>February 1st, 2016</b></div>
  </div>
  <div class="fair-rsvp">To Participate in our Spirit Fair Music,<br>Song, Dance RSVP by <b>February 12th, 2016</b></div>
  <div class="team-photo" role="img" aria-label="Photo of teen volunteers standing together"></div>

  <div class="about">
    <p>The purpose of this Crossroads Teen Summit is to bring together young people from diverse ethnic, cultural, and religious backgrounds, and to engage them in dialogue. True dialogue is a conversation on a common subject between two or more persons of differing points of view and/or backgrounds.</p>
    <p>The forum itself involves having eight high school-age kids and one adult youth leader around each table to discuss a common question.<br>Our intent is to make each discussion group as religiously diverse as possible.</p>
    <p>The forum will be followed by the Spirit Fair where families of the participants are welcomed to join.<br>This event will include and Art gallery display of the teens, highlighting their expressions of faith</p>
  </div>

  <div class="art-photo" role="img" aria-label="Teen painting of a sunset landscape"></div>
  <div class="art-frame"></div>
  <div class="art-box">
    <div class="big">Art work</div>
    <div class="small">Must be Submitted by</div>
    <div class="small">March 1st, 2015</div>
  </div>
  <div class="back-bar"></div>
  <div class="contact">
    <span><svg><use href="#icon-phone"/></svg>(555) 014-2288</span>
    <span><svg><use href="#icon-mail"/></svg>UTAHVorg@mailbox.example</span>
    <span><svg><use href="#icon-globe"/></svg>www.utahv.org</span>
  </div>
</section>
</body>
</html>
```